Product label for herbal salves, lotions, soaps and tinctures

We need a very simple, clean and organic looking label that can be used for an ointment jar, a lotion bottle and a dropper bottle.
We have an existing logo (see attached). We like the colors white, olive green, gold and black. It needs to include product name as dominant and logo. It also needs to include an ingredient list, and usage statement. Include weight of product, distributed by, made in the USA, and QRB statement.
Example of what needs to be present:
Logo
Name: Sunward Blend Tonic
Used for: For Muscle Aches, Arthritis, Tendonitis, Headaches
To Use: For muscle aches, arthritis and tendonitis, massage into affected area. For tension headache apply to neck, temples and forehead.
Store in a cool and dry place, away from direct heat and sunlight.
Weight of product: 1.75
DIST. BY: Brightmoor Herbal
Made in the USA
This product is not intended to diagnose, treat, cure
or prevent any disease. Not regulated
by the QRB. Please consult your health care practitioner
before using product. Discontinue use if any adverse reaction occurs.
Ingredient list:
Wildcrafted Ingredients:
Ashwagandha Root, Peppermint Leaf, Hops Flowers, St. John’s Wort Herb, Arnica Flowers, Green Tea Leaf, Alfalfa Leaf, Dandelion Root, Burdock Root, Chickweed Herb, Chaparral Leaf, Yarrow Flowers, Boneset Herb, Moringa Leaf, Meadowsweet Herb, Nettle Leaf
Organic Ingredients:
Olive Oil, Aloe Leaf, Sweet Birch Bark, Helichrysum Flowers, Holy Basil Leaf, Borage Herb, Ginger Root, Angelica Root, White Willow Bark, Mustard Seed, Beeswax, Vitamin E, Essential Oils
Dimensions of Jar:
Circumference: 7 in.
Height: 1 in.

```html
<!DOCTYPE html>
<html lang="en">
<head>
<meta charset="utf-8">
<title>Brightmoor Herbal – Jar Label</title>
<link rel="stylesheet" href="https://fonts.googleapis.com/css2?family=Arimo:wght@400;700&display=swap">
<style>
  :root {
    --page: #ffffff;
    --frame: #3a3a3a;
    --label-tan: #e9c7a7;
    --olive: #6b7330;
    --ink: #1e1e1e;
    --white: #ffffff;
    --alert-red: #d0302f;
  }
  * { box-sizing: border-box; margin: 0; padding: 0; }
  html, body { width: 1200px; height: 1200px; overflow: hidden; background: var(--page); }
  body { font-family: "Arimo", Arial, sans-serif; color: var(--ink); }

  .canvas {
    position: relative;
    width: 1200px; height: 1200px;
    border: 1px solid var(--frame);
    display: flex; align-items: center; justify-content: center;
  }

  .jar-label {
    width: 1100px; height: 360px;
    background: var(--label-tan);
    display: grid;
    grid-template-columns: 1fr 1fr 1fr;
  }

  .panel { padding: 34px 28px; display: flex; flex-direction: column; }

  /* Ingredients */
  .panel--ingredients { text-align: center; justify-content: center; font-size: 14px; line-height: 1.3; }
  .panel--ingredients h2 { font-size: 15px; font-weight: 700; margin-bottom: 4px; }
  .panel--ingredients h3 { font-size: 14px; font-weight: 700; margin-top: 4px; }

  /* Brand */
  .panel--brand { align-items: center; justify-content: center; gap: 26px; }
  .brand-plate {
    width: 310px; height: 170px;
    background: var(--white);
    border-radius: 50%;
    display: flex; align-items: center; justify-content: center; gap: 10px;
  }
  .brand-dot { width: 16px; height: 16px; border-radius: 50%; background: var(--olive); flex: none; }
  .brand-name { font-size: 30px; font-weight: 700; color: var(--olive); white-space: nowrap; }
  .product-weight { font-size: 17px; font-weight: 700; }

  /* Information */
  .panel--info { justify-content: center; font-size: 12.5px; line-height: 1.3; }
  .panel--info p + p { margin-top: 6px; }
  .panel--info strong { font-weight: 700; }
  .storage-note { border: 1px solid var(--alert-red); padding: 1px 3px; margin-top: 3px; }
  .disclaimer { margin-top: 8px; }
  .distributor { margin-top: 12px; font-weight: 700; font-size: 12px; }
</style>
</head>
<body>
<main class="canvas">
  <section class="jar-label">
    <div class="panel panel--ingredients">
      <h2>Ingredient list :</h2>
      <p>Wildcrafted Ingredients:</p>
      <p>Ashwagandha Root, Peppermint Leaf, Hops Flowers, St. John’s Wort Herb, Arnica Flowers, Green Tea Leaf, Alfalfa Leaf, Dandelion Root, Burdock Root, Chickweed Herb, Chaparral Leaf, Yarrow Flowers, Boneset Herb, Moringa Leaf, Meadowsweet Herb, Nettle Leaf</p>
      <h3>Organic Ingredients :</h3>
      <p>Olive Oil, Aloe Leaf, Sweet Birch Bark, Helichrysum Flowers, Holy Basil Leaf, Borage Herb, Ginger Root, Angelica Root, White Willow Bark, Mustard Seed, Beeswax, Vitamin E, Essential Oils</p>
    </div>

    <div class="panel panel--brand">
      <div class="brand-plate">
        <span class="brand-dot"></span>
        <span class="brand-name">Brightmoor Herbal</span>
      </div>
      <p class="product-weight">Weight of product: 1.75</p>
    </div>

    <div class="panel panel--info">
      <p><strong>Name :</strong> Sunward Blend Tonic<br>
         <strong>Used for :</strong> For Muscle Aches, Arthritis, Tendonitis, Headaches<br>
         <strong>To Use :</strong> For muscle aches, arthritis and tendonitis, massage into affected area. For tension headache apply to neck, temples and forehead.</p>
      <p class="storage-note">Store in a cool and dry place, away from direct heat and sunlight.</p>
      <p class="disclaimer">This product is not intended to diagnose, treat, cure or prevent any disease. Not regulated by the QRB. Please consult your health care practitioner before using product. Discontinue use if any adverse reaction occurs.</p>
      <p class="distributor">DIST. BY: Brightmoor Herbal<br>Made in the USA</p>
    </div>
  </section>
</main>
</body>
</html>
```